Full service residential and commercial painting
Finest quality attention to detail
All workmanship guaranteed
Email :brunomdufay@postvale.fr
Mobile: 0417386250
Industry/Entity Type
Residential
Contact Information for Business Card
Marten Dufay painting & decorating
Requirements
Nice to have
- Am thinking about someone can be painting my name on the card with MD painting with the logos of brush,pot tray and roller sleeves

```html
<!DOCTYPE html>
<html lang="en">
<head>
<meta charset="utf-8">
<title>MD painting – business card</title>
<link rel="stylesheet" href="https://fonts.googleapis.com/css2?family=Open+Sans:wght@400;600&display=swap">
<style>
  :root {
    --backdrop: #2b2a2a;
    --card-deep: #0f2a30;
    --card-mid: #173c44;
    --card-glow: #1d5663;
    --paint-pink: #e0245e;
    --ink-blue: #2c9fd9;
    --can-light: #e8eef0;
    --can-teal: #2f8fa0;
  }
  * { box-sizing: border-box; margin: 0; padding: 0; }
  html, body {
    width: 1200px; height: 816px; overflow: hidden;
    background: var(--backdrop);
    font-family: "Open Sans", Calibri, sans-serif;
  }
  .business-card {
    position: absolute; left: 80px; top: 111px;
    width: 1040px; height: 594px;
    background: radial-gradient(ellipse at 30% 85%, var(--card-glow) 0%, var(--card-mid) 35%, var(--card-deep) 100%);
    overflow: hidden;
  }
  .paint-splash {
    position: absolute; left: 0; top: 40px;
    width: 250px; height: 230px;
    background: var(--paint-pink);
    border-radius: 0 48% 40% 0;
  }
  .paint-cans {
    position: absolute; left: 190px; top: 330px;
    width: 270px; height: 264px;
    background: radial-gradient(ellipse at 50% 55%, var(--can-light) 0%, var(--can-teal) 45%, rgba(23,60,68,0) 72%);
  }
  .brand-name {
    position: absolute; left: 330px; top: 70px;
    font-size: 96px; font-weight: 600;
    color: var(--paint-pink); letter-spacing: 1px;
    line-height: 1;
  }
  .contact-block {
    position: absolute; right: 80px; top: 248px;
    text-align: right; color: var(--ink-blue);
  }
  .company-line {
    font-size: 25px; font-variant: small-caps; letter-spacing: 1px;
    margin-bottom: 10px;
  }
  .contact-line {
    font-size: 28px; display: flex; justify-content: flex-end;
    align-items: center; gap: 14px; margin-bottom: 12px;
  }
  .contact-line svg { width: 26px; height: 26px; }
  .tagline {
    position: absolute; right: 80px; top: 462px;
    text-align: right; color: var(--ink-blue);
    font-size: 22px; line-height: 36px;
  }
  .tagline .divider { color: var(--paint-pink); padding: 0 6px; }
</style>
</head>
<body>
  <section class="business-card">
    <div class="paint-splash" role="img" aria-label="Pink paint splash"></div>
    <div class="paint-cans" role="img" aria-label="Open paint tins in bright colours with a brush"></div>

    <h1 class="brand-name">MD painting</h1>

    <div class="contact-block">
      <p class="company-line">Marten Dufay painting &amp; decorating</p>
      <p class="contact-line">0417386250
        <svg viewBox="0 0 26 26" aria-hidden="true">
          <rect width="26" height="26" rx="3" fill="var(--paint-pink)"/>
          <path d="M8 5c-1.5 1-2 2.5-1.5 4.5 1.2 4.5 5 8.8 9.5 10.4 2 .7 3.5.2 4.5-1.2l-3-3-2 1.2c-2-1-4-3-5-5l1.2-2z" fill="var(--card-deep)"/>
        </svg>
      </p>
      <p class="contact-line">brunomdufay@postvale.fr
        <svg viewBox="0 0 26 26" aria-hidden="true">
          <rect x="2" y="6" width="22" height="14" fill="none" stroke="var(--paint-pink)" stroke-width="2.4"/>
          <path d="M2 6l11 8 11-8" fill="none" stroke="var(--paint-pink)" stroke-width="2.4"/>
        </svg>
      </p>
    </div>

    <div class="tagline">
      <p>Full service residential and commercial painting</p>
      <p>Finest quality attention to detail<span class="divider">|</span>All workmanship guaranteed</p>
    </div>
  </section>
</body>
</html>
```